Independence Day Graphics for Sale

I want to create 10 social media graphics (new Pictora size 4:5 (1080 x 1350 pixels) focusing on our July 4th Sale Graphics, using any of the pics attached. Use the attached pics, NO RANDOM STOCK PHOTOGRAPHY. For the color scheme of the graphics, they should all be complementary to the product colors in the photos.
You can add any of the photos attached but none are required. You can do some of the graphics in all text. I mainly need BOLD text that says one of the headlines (10 total) SEE ATTACHED WORD DOCUMENT for the headlines to use.

Target Market(s)

women looking to lose weight

Requirements
Must have
• pics attached and text attached

```html
<!DOCTYPE html>
<html lang="en">
<head>
<meta charset="utf-8">
<title>July 4th Sale Social Graphics</title>
<link href="https://fonts.googleapis.com/css2?family=Anton&display=swap" rel="stylesheet">
<style>
  :root {
    --canvas-bg: #cfcfcf;
    --plum: #8a2a7c;
    --plum-deep: #7a1f6c;
    --plum-glow: #c65aa8;
    --sun-yellow: #f8ee1a;
    --white: #ffffff;
    --photo-warm: #b9a59a;
    --photo-light: #e8e2dc;
  }
  * { margin: 0; padding: 0; box-sizing: border-box; }
  html, body { width: 1200px; height: 611px; overflow: hidden; background: var(--canvas-bg); }
  .board { position: relative; width: 1200px; height: 611px; font-family: "Anton", "Oswald", sans-serif; }
  .tile {
    position: absolute; width: 224px; height: 280px; overflow: hidden;
    background: radial-gradient(ellipse at 50% 35%, var(--plum-glow) 0%, var(--plum) 55%, var(--plum-deep) 100%);
  }
  .row-top { top: 21px; }
  .row-bottom { top: 311px; }
  .col-1 { left: 19px; } .col-2 { left: 253px; } .col-3 { left: 489px; } .col-4 { left: 723px; } .col-5 { left: 958px; }

  .model-photo {
    position: absolute; right: 0; top: 0; width: 46%; height: 100%;
    background: linear-gradient(90deg, rgba(185,165,154,0) 0%, var(--photo-warm) 25%, #8f7b72 100%);
  }
  .product-photo {
    position: absolute; left: 8%; top: 68%; width: 88%; height: 24%;
    background: linear-gradient(180deg, var(--photo-light), #d7cfd8);
    border-radius: 6px; opacity: .92;
  }
  .product-row {
    position: absolute; left: 11%; top: 68%; width: 78%; height: 26%;
    background: linear-gradient(180deg, #f4f2f4, #dcd6df);
    border-radius: 6px;
  }
  .product-inline {
    position: absolute; left: 22px; top: 58px; width: 76px; height: 34px;
    background: linear-gradient(180deg, #f4f2f4, #dcd6df); border-radius: 4px;
  }

  .copy { position: absolute; line-height: .98; letter-spacing: .2px; }
  .copy span { display: block; white-space: nowrap; }
  .y { color: var(--sun-yellow); }
  .w { color: var(--white); }
  .center { left: 0; width: 100%; text-align: center; text-transform: uppercase; }
</style>
</head>
<body>
<main class="board">

  <section class="tile row-top col-1">
    <div class="model-photo" role="img" aria-label="Smiling woman holding a supplement bottle"></div>
    <div class="product-photo" role="img" aria-label="Row of supplement bottles on a counter"></div>
    <div class="copy" style="left:17px; top:16px; font-size:29px;">
      <span class="y">Biggest</span><span class="y">4th of July</span><span class="y">Sale Ever!</span>
      <span class="w">25% OFF</span><span class="w">Sitewide</span>
    </div>
  </section>

  <section class="tile row-top col-2">
    <div class="model-photo" role="img" aria-label="Smiling woman presenting supplements"></div>
    <div class="product-photo" role="img" aria-label="Row of supplement bottles on a counter"></div>
    <div class="copy" style="left:17px; top:16px; font-size:29px;">
      <span class="w">Historic</span><span class="w">4th of July</span><span class="w">Sale Ever!</span>
      <span class="y">25% OFF</span><span class="y">Sitewide</span>
    </div>
  </section>

  <section class="tile row-top col-3">
    <div class="model-photo" role="img" aria-label="Smiling woman holding a supplement bottle"></div>
    <div class="product-photo" role="img" aria-label="Row of supplement bottles on a counter"></div>
    <div class="copy" style="left:17px; top:16px; font-size:31px;">
      <span class="w">Mega</span><span class="w">Summer</span><span class="w">Blowout!</span>
      <span class="y" style="font-size:28px;">25% OFF</span><span class="y" style="font-size:28px;">Everything</span>
    </div>
  </section>

  <section class="tile row-top col-4">
    <div class="model-photo" role="img" aria-label="Smiling woman standing behind supplement bottles"></div>
    <div class="copy" style="left:15px; top:26px;">
      <span class="y" style="font-size:64px; line-height:.95;">LAST</span>
      <span class="y" style="font-size:40px;">CHANCE</span>
      <span class="w" style="font-size:32px;">25% OFF</span>
      <span class="w" style="font-size:42px;">TIME IS</span>
      <span class="w" style="font-size:22px;">RUNNING OUT!</span>
    </div>
  </section>

  <section class="tile row-top col-5">
    <div class="copy center" style="top:26px;">
      <span class="w" style="font-size:38px;">THE LOWEST</span>
      <span class="y" style="font-size:24px;">PRICES WE'VE EVER</span>
      <span class="w" style="font-size:50px;">OFFERED!</span>
      <span class="y" style="font-size:50px;">25% OFF</span>
      <span class="w" style="font-size:40px;">EVERYTHING</span>
    </div>
  </section>

  <section class="tile row-bottom col-1">
    <div class="copy center" style="top:18px;">
      <span class="y" style="font-size:46px;">JULY 4TH</span>
      <span class="w" style="font-size:38px;">MEGA SALE!</span>
      <span class="y" style="font-size:46px;">25% OFF</span>
      <span class="w" style="font-size:38px;">EVERYTHING</span>
    </div>
    <div class="product-row" role="img" aria-label="Four supplement bottles in a row"></div>
  </section>

  <section class="tile row-bottom col-2">
    <div class="product-inline" role="img" aria-label="Small group of supplement bottles"></div>
    <div class="copy center" style="top:14px;">
      <span class="y" style="font-size:44px;">ONE-TIME</span>
      <span class="w" style="font-size:40px; padding-left:108px; text-align:left;">ONLY</span>
      <span class="y" style="font-size:50px;">25% OFF</span>
      <span class="w" style="font-size:30px;">OF EVERYTHING!</span>
    </div>
    <div class="product-row" role="img" aria-label="Four supplement bottles in a row"></div>
  </section>

  <section class="tile row-bottom col-3">
    <div class="copy center" style="top:22px;">
      <span class="w" style="font-size:46px;">25% OFF</span>
      <span class="y" style="font-size:28px;">STOCK-UP EVENT</span>
      <span class="w" style="font-size:46px;">25% OFF</span>
      <span class="y" style="font-size:26px;">ALL SUPPLEMENTS</span>
    </div>
    <div class="product-row" role="img" aria-label="Four supplement bottles in a row"></div>
  </section>

  <section class="tile row-bottom col-4">
    <div class="copy center" style="top:24px;">
      <span class="w" style="font-size:36px;">OUR BIGGEST</span>
      <span class="y" style="font-size:29px;">DISCOUNT EVER!</span>
      <span class="w" style="font-size:46px;">25% OFF</span>
      <span class="y" style="font-size:40px;">EVERYTHING</span>
    </div>
    <div class="product-row" role="img" aria-label="Four supplement bottles in a row"></div>
  </section>

  <section class="tile row-bottom col-5">
    <div class="copy center" style="top:36px;">
      <span class="w" style="font-size:40px;">DON'T WAIT!</span>
      <span class="y" style="font-size:50px;">25% OFF</span>
      <span class="w" style="font-size:44px;">ENDS SOON</span>
    </div>
    <div class="product-row" role="img" aria-label="Four supplement bottles in a row"></div>
  </section>

</main>
</body>
</html>
```